Water Bottle Design

We are launching a water bottle and need a impactful design.

Target Market(s)

health conscious hipsters

Font styles to use
Sans Serif

Requirements
Must have
• Please include the logo (included) on one side of the bottle and these words on the other side of the bottle. "It’s simple, REUSE this bottle every day. Your action, will REDUCE the amount of waste produced. SAVE your body from drinking the harmful contaminants in your water from Non-BPA plastics. HELP someone else because proceeds from your purchase will help homeless veterans.
• We’re just two dudes that like to drink water and help people. #PayItFoward"
• Use a total of two colors
• UPDATE: You do not have to use the bottle on the logo.
Nice to have
• The bottle itself is 34 ounces and looks like a normal water bottle. I will include the image in the files. We would need to be able to change the colors easily.
Should not have
• Do not use more than two colors. Colors should not be important to the design at this point.

```html
<!DOCTYPE html>
<html lang="en">
<head>
<meta charset="utf-8">
<title>Water Bottle Message Panel</title>
<link rel="stylesheet" href="https://fonts.googleapis.com/css2?family=Roboto:wght@300&family=Archivo+Narrow:wght@700&display=swap">
<style>
  :root {
    --bottle-blue: #5b67e2;
    --ink-white: #ffffff;
  }
  html, body {
    margin: 0;
    padding: 0;
    width: 1200px;
    height: 1056px;
    overflow: hidden;
    background: var(--bottle-blue);
  }
  .message-panel {
    position: relative;
    width: 1200px;
    height: 1056px;
    color: var(--ink-white);
  }
  .headwords {
    position: absolute;
    left: 0;
    top: 0;
    width: 1200px;
    height: 1056px;
  }
  .headword {
    font-family: "Roboto", sans-serif;
    font-weight: 300;
    font-size: 405px;
    fill: var(--ink-white);
  }
  .copy-line {
    position: absolute;
    left: 138px;
    width: 832px;
    margin: 0;
    font-family: "Archivo Narrow", sans-serif;
    font-weight: 700;
    font-size: 36px;
    line-height: 36px;
    text-transform: uppercase;
    white-space: nowrap;
    display: flex;
    justify-content: space-between;
  }
  .copy-line.spaced { font-size: 24px; line-height: 24px; }
  .top-line { top: 0; font-size: 28px; line-height: 28px; }
  .body-line-1 { top: 341px; }
  .body-line-2 { top: 398px; }
  .plastics-line { top: 466px; }
  .help-line-1 { top: 803px; }
  .help-line-2 { top: 863px; }
</style>
</head>
<body>
<main class="message-panel">
  <svg class="headwords" viewBox="0 0 1200 1056" width="1200" height="1056">
    <text class="headword save-word" x="138" y="318" textLength="832" lengthAdjust="spacingAndGlyphs">SAVE</text>
    <text class="headword help-word" x="138" y="802" textLength="832" lengthAdjust="spacingAndGlyphs">HELP</text>
  </svg>

  <p class="copy-line top-line"><span>The</span><span>amount</span><span>of</span><span>waste</span><span>produced</span></p>

  <p class="copy-line body-line-1"><span>Your</span><span>body</span><span>from</span><span>drinking</span><span>the</span><span>harmful</span></p>
  <p class="copy-line body-line-2"><span>contaminants</span><span>in</span><span>your</span><span>water</span><span>from</span><span>non-BPA</span></p>
  <p class="copy-line spaced plastics-line"><span>P</span><span>L</span><span>A</span><span>S</span><span>T</span><span>I</span><span>C</span><span>S</span></p>

  <p class="copy-line help-line-1"><span>Someone</span><span>else</span><span>because</span><span>proceeds</span><span>from</span><span>your</span></p>
  <p class="copy-line help-line-2"><span>purchase</span><span>will</span><span>help</span><span>homeless</span><span>veterans.</span></p>
</main>
</body>
</html>
```